Poster for a Bicycle show/Expo

We need a poster for a Bicycle show/Expo and sustainable transport. Exhibitors will sell bikes, cycling clothing, accessories, etc. ...
This show is annual and the Poster is for the 2016 edition.

Your concept must be compatible in a landscape format. (We will ourselves adaptations of different formats.)
Width: 210 mm
Height: 297 mm
It's necessary for us to have the source file (vector) for make, later, the different format (flyers, website, ...)

Content of the Poster:
- 1 big picture (one of the two attached)
- Big title (typo-title worked): « Foire du Rouet » (« Salon » or « Salon du » can be small and « Vélo » big.)
- Subtitle: « et de la mobilité durable »
- Date: « 18, 19 et 20 mars 2016 » or « 18-20 mars 2016 »
- Place: « Halle RTP - Gare de Plantaz »
- Text line 1: « www.foire-du-rouet.ch »
- Text line 2: « Entrée gratuite »
- Text line 3: « Ve 18 mars de 17h à 20h - Sa 19 mars de 10h à 18h - Di 20 mars de 10h à 17h »
- Please, leave a zone in the poster for sponsors logos
(The predominant information (most visible) are: « Vélo » and « 18, 19 et 20 mars 2016 » or « 18-20 mars 2016 »)

Target Market(s)

Bicycle fan

Industry/Entity Type

Sporting Good

Font styles to use
Serif
Sans Serif

Colors
add136
ffffff
ec1f27

Requirements
Must have
• The style must be modern, dynamic, bright colors.

```html
<!DOCTYPE html>
<html lang="fr">
<head>
<meta charset="utf-8">
<title>Foire du Rouet 2016</title>
<link rel="stylesheet" href="https://fonts.googleapis.com/css2?family=Archivo+Black&family=Tinos:ital,wght@0,400;0,700;1,400&display=swap">
<style>
  :root {
    --sky-top: #2f7fd0;
    --sky-mid: #5aa2e4;
    --sky-low: #9cc8ef;
    --green: #add136;
    --white: #ffffff;
    --red: #ec1f27;
    --ink: #1f4e8c;
  }
  * { margin: 0; padding: 0; box-sizing: border-box; }
  html, body { width: 849px; height: 1200px; overflow: hidden; }
  body { font-family: "Tinos", "Times New Roman", serif; }
  .poster {
    position: relative;
    width: 849px;
    height: 1200px;
    overflow: hidden;
    background: linear-gradient(180deg, var(--sky-top) 0%, var(--sky-mid) 45%, var(--sky-low) 85%, #c9e0f5 100%);
  }
  .sky-photo {
    position: absolute; inset: 0;
    background:
      radial-gradient(ellipse 260px 70px at 120px 1110px, rgba(255,255,255,0.75), transparent 70%),
      radial-gradient(ellipse 300px 60px at 720px 1080px, rgba(255,255,255,0.6), transparent 70%),
      radial-gradient(ellipse 200px 50px at 40px 40px, rgba(255,255,255,0.5), transparent 70%);
  }
  .cloud-bicycle {
    position: absolute;
    left: 250px; top: 0;
    width: 580px; height: 310px;
    border-radius: 50%;
    background: radial-gradient(ellipse at 50% 50%, rgba(255,255,255,0.85) 0%, rgba(240,247,255,0.6) 40%, rgba(255,255,255,0.2) 65%, transparent 72%);
  }
  .kicker {
    position: absolute;
    left: 120px; top: 282px;
    font-family: "Archivo Black", "Arial Black", sans-serif;
    font-size: 34px;
    color: var(--green);
    letter-spacing: 1px;
  }
  .headline {
    position: absolute;
    left: 118px; top: 300px;
    font-family: "Archivo Black", "Arial Black", sans-serif;
    font-weight: 400;
    font-size: 215px;
    line-height: 1.2;
    letter-spacing: -3px;
    color: var(--white);
  }
  .subtitle {
    position: absolute;
    left: 0; right: 0; top: 572px;
    text-align: center;
    font-size: 34px;
    font-weight: 700;
    color: var(--green);
  }
  .venue {
    position: absolute;
    left: 212px; top: 634px;
    width: 560px; height: 50px;
    background: rgba(255,255,255,0.9);
    color: var(--ink);
    font-size: 31px;
    font-weight: 700;
    line-height: 50px;
    text-align: center;
  }
  .info-panel {
    position: absolute;
    left: 85px; top: 740px;
    width: 695px; height: 290px;
    background: rgba(255,255,255,0.85);
  }
  .dates {
    position: absolute;
    left: 15px; top: 22px;
    width: 235px;
    color: var(--green);
    font-weight: 700;
    text-align: center;
    line-height: 1;
  }
  .dates .days { font-size: 76px; display: block; }
  .dates .month { font-size: 70px; display: block; letter-spacing: 1px; }
  .dates .year { font-size: 72px; display: block; }
  .hours {
    position: absolute;
    left: 250px; top: 48px;
    list-style: none;
    color: var(--ink);
    font-size: 25px;
    line-height: 35px;
  }
  .rule {
    position: absolute;
    left: 250px; top: 170px;
    width: 420px; height: 2px;
    background: var(--ink);
    opacity: 0.4;
  }
  .entry {
    position: absolute;
    left: 425px; top: 985px;
    color: var(--red);
    font-size: 36px;
    font-style: italic;
  }
  .website {
    position: absolute;
    left: 0; right: 0; top: 1124px;
    text-align: center;
    color: var(--white);
    font-size: 40px;
    font-weight: 700;
    letter-spacing: 5px;
  }
</style>
</head>
<body>
  <main class="poster">
    <div class="sky-photo" role="img" aria-label="Ciel bleu avec nuages"></div>
    <div class="cloud-bicycle" role="img" aria-label="Vélo dessiné en nuage dans le ciel"></div>

    <p class="kicker">FOIRE DU</p>
    <h1 class="headline">Rouet</h1>
    <p class="subtitle">et de la mobilité durable</p>

    <p class="venue">Halle RTP - Gare de Plantaz</p>

    <section class="info-panel">
      <p class="dates">
        <span class="days">18-20</span>
        <span class="month">MARS</span>
        <span class="year">2016</span>
      </p>
      <ul class="hours">
        <li>Vendredi 18 mars de 17h à 20h</li>
        <li>Samedi 19 mars de 10h à 18h</li>
        <li>Dimanche 20 mars de 10h à 17h</li>
      </ul>
      <div class="rule"></div>
    </section>

    <p class="entry">Entrée gratuite</p>

    <p class="website">www.foire-du-rouet.ch</p>
  </main>
</body>
</html>
```